Design a box for EV Charging Cables - Electric Cars

https://files.plomtrex.example/doc/7qRwLm2ZxNa9/view

We are looking to design a box to package our EV charging cables. This box needs to be 40cm x 40cm x 11cm.

It needs to include:
- Our logo
- Images of our products
- Accreditations

My websites are:
https://voltharbor.co.uk/
https://www.plugmerrow.co.uk/
https://www.zandrel-amp.co.uk/

Logo:
https://pixdrop.example/Kq8Tz2L
https://pixdrop.example/Rw4Hn9B
https://pixdrop.example/Jd7Pv3X
https://pixdrop.example/Ny6Qb5G

Rather than having a list of products. I would like to have tick boxes:
1st tick box: Connector Type From: (Type 2, 3 Pin),
2nd tick box: Connector Type To: (Type 1, Type 2),
3rd tick box: Amp/Charge Speed (13amp/16amp/32amp/32amp - 3 Phase)
4th tick box: Length (5m/10m/15m)

Target Market(s)

People who own electric cars

Industry/Entity Type

Automotive

Colors

Designer to choose colors to be used in the design.

Requirements
Must have
• Our colours, logo, list of products we sell
Nice to have
• Rather than having a list of products. I would like to have tick boxes: 1st tick box should be: Connector Type From: (Type 2, 3 Pin), Connector Type To: (Type 1, Type 2), Third: Amp/Charge Speed (13amp/16amp/32amp/32amp - 3 Phase) Third: Length (5m/10m/15m)
Should not have
• Transparent Section

```html
<!DOCTYPE html>
<html lang="en">
<head>
<meta charset="utf-8">
<title>Zandrel Amp – EV Charging Cables Box</title>
<link href="https://fonts.googleapis.com/css2?family=Archivo+Black&family=Roboto+Condensed:wght@700&display=swap" rel="stylesheet">
<style>
  :root {
    --stage: #8dbf34;
    --panel: #f1f1f1;
    --green-deep: #5c9a1f;
    --green-mid: #7cb82a;
    --green-lime: #b5dc3a;
    --green-pale: #c9e29a;
    --ink: #1d1f27;
    --grey: #7b7b7f;
    --white: #ffffff;
  }
  * { box-sizing: border-box; margin: 0; padding: 0; }
  html, body { width: 1200px; height: 960px; overflow: hidden; }
  body {
    background: var(--stage);
    position: relative;
    font-family: "Roboto Condensed", Arial, sans-serif;
  }
  .box-net { position: absolute; left: 190px; top: 110px; width: 820px; height: 740px; }

  /* Top panel */
  .panel-top {
    position: absolute; left: 180px; top: 0; width: 640px; height: 180px;
    background: linear-gradient(120deg, var(--green-deep) 0%, var(--green-lime) 45%, var(--green-mid) 75%, var(--green-pale) 100%);
    display: flex; align-items: center; justify-content: center;
  }
  .panel-top .brand-name { color: var(--white); font-size: 38px; }

  /* Side panel */
  .panel-side {
    position: absolute; left: 0; top: 180px; width: 180px; height: 560px;
    background: var(--panel);
    border-right: 1px solid #d8d8d8;
    overflow: hidden;
  }
  .side-title {
    position: absolute; left: 50%; top: 50%;
    transform: translate(-50%, -50%) rotate(90deg);
    white-space: nowrap; font-family: "Archivo Black", Arial, sans-serif;
    line-height: 0.9; text-align: left;
  }
  .side-title .big { display: block; font-size: 110px; color: var(--green-mid); }
  .side-title .sub { display: block; font-size: 44px; color: var(--grey); }
  .side-title .sub-top { font-size: 30px; }

  /* Front panel */
  .panel-front {
    position: absolute; left: 180px; top: 180px; width: 640px; height: 560px;
    background: var(--panel); overflow: hidden;
  }
  .brand-name {
    font-family: "Roboto Condensed", Arial, sans-serif; font-weight: 700;
    letter-spacing: 4px; text-transform: uppercase;
  }
  .front-brand {
    position: absolute; left: 0; right: 0; top: 50px; text-align: center;
    color: var(--green-deep); font-size: 40px;
  }
  .rule { position: absolute; height: 6px; border-radius: 3px; background: var(--green-deep); }
  .rule-left { left: 0; top: 168px; width: 420px; }
  .rule-right { left: 500px; top: 118px; width: 140px; }

  .hero-ev {
    position: absolute; left: 0; top: 170px;
    font-family: "Archivo Black", Arial, sans-serif; font-size: 270px; line-height: 1;
    color: var(--green-mid); letter-spacing: -8px;
  }
  .hero-title {
    position: absolute; left: 300px; top: 215px;
    font-family: "Archivo Black", Arial, sans-serif; color: var(--ink); line-height: 0.95;
  }
  .hero-title .line-1 { display: block; font-size: 40px; padding-left: 14px; }
  .hero-title .line-2 { display: block; font-size: 54px; }

  .product-photo {
    position: absolute; left: 0; top: 380px; width: 420px; height: 180px;
    border-radius: 0 26px 0 0;
    background: linear-gradient(135deg, var(--green-mid) 0%, var(--green-lime) 55%, var(--green-deep) 100%);
  }
  .product-photo-connector {
    position: absolute; left: 150px; top: 300px; width: 160px; height: 260px;
    border-radius: 40px 40px 0 0;
    background: linear-gradient(180deg, #2a2d38 0%, var(--ink) 100%);
  }

  .spec-list { position: absolute; left: 436px; top: 338px; width: 190px; list-style: none; }
  .spec-item { position: relative; padding-left: 30px; margin-bottom: 10px; }
  .spec-item .tick { position: absolute; left: 0; top: 18px; width: 22px; height: 18px; }
  .spec-label { font-size: 15px; color: var(--green-deep); line-height: 1.2; }
  .spec-label strong { color: var(--ink); }
  .spec-options { display: flex; justify-content: space-between; gap: 6px; margin-top: 3px; }
  .pill {
    background: var(--green-deep); color: var(--ink); border-radius: 4px;
    font-size: 14px; padding: 1px 8px; white-space: nowrap;
  }
  .pill.small { font-size: 9px; padding: 3px 6px; width: 100%; text-align: center; }
  .spec-inline { display: flex; align-items: center; justify-content: space-between; }
  .spec-inline .spec-label { color: var(--ink); }
  .spec-inline .pill.small { width: 100px; }
</style>
</head>
<body>
  <div class="box-net">
    <section class="panel-top" aria-label="Box lid">
      <span class="brand-name">Zandrel Amp</span>
    </section>

    <section class="panel-side" aria-label="Box side">
      <div class="side-title">
        <span class="big">EV</span>
        <span class="sub sub-top">CHARGING</span>
        <span class="sub">CABLES</span>
      </div>
    </section>

    <section class="panel-front" aria-label="Box front">
      <div class="front-brand brand-name">Zandrel Amp</div>
      <div class="rule rule-left"></div>
      <div class="rule rule-right"></div>

      <div class="hero-ev">EV</div>
      <h1 class="hero-title">
        <span class="line-1">CHARGING</span>
        <span class="line-2">CABLES</span>
      </h1>

      <div class="product-photo" role="img" aria-label="Green swirl backdrop behind the charging cable"></div>
      <div class="product-photo-connector" role="img" aria-label="Photo of a black EV charging connector with cable"></div>

      <ul class="spec-list">
        <li class="spec-item">
          <svg class="tick" viewBox="0 0 22 18"><path d="M2 9 L8 15 L20 2" fill="none" stroke="var(--green-deep)" stroke-width="3"/></svg>
          <div class="spec-label">Connector Type <strong>From:</strong></div>
          <div class="spec-options"><span class="pill">Type 2</span><span class="pill">3 Pin</span></div>
        </li>
        <li class="spec-item">
          <svg class="tick" viewBox="0 0 22 18"><path d="M2 9 L8 15 L20 2" fill="none" stroke="var(--green-deep)" stroke-width="3"/></svg>
          <div class="spec-label">Connector Type <strong>To:</strong></div>
          <div class="spec-options"><span class="pill">Type 1</span><span class="pill">Type 2</span></div>
        </li>
        <li class="spec-item">
          <svg class="tick" viewBox="0 0 22 18"><path d="M2 9 L8 15 L20 2" fill="none" stroke="var(--green-deep)" stroke-width="3"/></svg>
          <div class="spec-label">Amp/Charge <strong>Speed:</strong></div>
          <div class="spec-options"><span class="pill small">13amp/ 16amp/ 32amp - 3 Phase</span></div>
        </li>
        <li class="spec-item spec-inline">
          <svg class="tick" viewBox="0 0 22 18" style="top:2px"><path d="M2 9 L8 15 L20 2" fill="none" stroke="var(--green-deep)" stroke-width="3"/></svg>
          <div class="spec-label">Length:</div>
          <span class="pill small">5m/10m/15m</span>
        </li>
      </ul>
    </section>
  </div>
</body>
</html>
```